Looking for an amazing business card for a thriving DJ business

We need a business card design for a DJ company based in South Florida. The DJ company specializes in weddings, parties, bar mitzvahs, corporate events, proms, and reunions. We are looking for a modern, simple business card design. The card should state DJ Marlow K.
Updates

The name on the card should be DJ Marlow K

Industry/Entity Type

Entertainment Industry

Contact Information for Business Card

DJ Marlow K
512.447.2086
atxdjmarlowk@quellmail.com
https://www.facebook.com/DjMarlowK/
https://www.instagram.com/djmarlow.k/
www.djmarlowk.net

Font styles to use
Serif
Sans Serif

Requirements
Must have
• My business card has to be awesome.
Should not have
• The card has to have personality.

```html
<!DOCTYPE html>
<html lang="en">
<head>
<meta charset="utf-8">
<title>DJ Marlow K – Business Card</title>
<link href="https://fonts.googleapis.com/css2?family=Roboto:wght@400;500;700&display=swap" rel="stylesheet">
<style>
  :root {
    --backdrop: #2b2b2b;
    --card: #ffffff;
    --bronze: #a8661f;
    --ink: #1c1c1c;
    --navy: #232a3d;
    --photo-light: #e9e6e2;
    --photo-dark: #6b4a36;
  }
  * { box-sizing: border-box; margin: 0; padding: 0; }
  html, body {
    width: 1200px; height: 900px; overflow: hidden;
    background: var(--backdrop);
    font-family: "Roboto", Arial, sans-serif;
  }
  .canvas {
    position: relative; width: 1200px; height: 900px;
  }
  .card {
    position: absolute; left: 285px;
    width: 630px; height: 360px;
    background: var(--card);
    border-radius: 0 180px 180px 0;
    box-shadow: 0 12px 30px rgba(0,0,0,.45);
  }
  .card--front { top: 70px; }
  .card--back { top: 470px; }

  .tagline {
    position: absolute; left: 56px; top: 128px; width: 260px;
    color: var(--bronze); font-size: 25px; line-height: 1.18;
    text-align: center; font-weight: 400;
  }
  .portrait {
    position: absolute; left: 316px; top: 46px;
    width: 268px; height: 268px; border-radius: 50%;
    border: 2px solid var(--bronze);
    padding: 4px;
  }
  .portrait__fill {
    width: 100%; height: 100%; border-radius: 50%;
    background: radial-gradient(circle at 30% 30%, var(--photo-dark) 0 18%, transparent 19%),
                linear-gradient(160deg, var(--photo-light), #ffffff 60%, var(--photo-light));
  }

  .name {
    position: absolute; left: 48px; top: 140px;
    color: var(--bronze); font-size: 30px; font-weight: 700;
  }
  .contacts {
    position: absolute; left: 48px; top: 188px;
    list-style: none; color: var(--ink); font-size: 16px;
  }
  .contacts li {
    display: flex; align-items: center; gap: 12px; height: 25px;
  }
  .contacts svg { width: 16px; height: 16px; flex: none; }
  .contacts .marker {
    width: 14px; height: 14px; border-radius: 3px; flex: none; margin: 0 1px;
    background: var(--bronze);
  }
  .brand-seal {
    position: absolute; left: 320px; top: 50px;
    width: 260px; height: 260px; border-radius: 50%;
    border: 3px solid var(--bronze);
    display: flex; align-items: center; justify-content: center;
  }
  .brand-seal__name {
    color: var(--navy); font-size: 34px; font-weight: 500;
  }
</style>
</head>
<body>
<div class="canvas">
  <section class="card card--front">
    <p class="tagline">DJ Luminaire's<br>Making your Event<br>Extraordinary</p>
    <div class="portrait">
      <div class="portrait__fill" role="img" aria-label="Portrait photo of the DJ in a white suit"></div>
    </div>
  </section>

  <section class="card card--back">
    <h1 class="name">DJ Marlow K</h1>
    <ul class="contacts">
      <li>
        <svg viewBox="0 0 24 24" aria-hidden="true"><path fill="#a8661f" d="M6.6 10.8a15.5 15.5 0 0 0 6.6 6.6l2.2-2.2c.3-.3.7-.4 1-.2 1.1.4 2.3.6 3.6.6.6 0 1 .4 1 1V20c0 .6-.4 1-1 1A17 17 0 0 1 3 4c0-.6.4-1 1-1h3.5c.6 0 1 .4 1 1 0 1.3.2 2.5.6 3.6.1.3 0 .7-.2 1z"/></svg>
        512.447.2086
      </li>
      <li>
        <svg viewBox="0 0 24 24" aria-hidden="true"><rect x="2" y="5" width="20" height="14" rx="1" fill="#a8661f"/><path d="M2 6l10 7 10-7" fill="none" stroke="#fff" stroke-width="1.6"/></svg>
        atxdjmarlowk@quellmail.com
      </li>
      <li><span class="marker"></span>www.facebook.com/DjMarlowK</li>
      <li><span class="marker"></span>www.instagram.com/djmarlow.k</li>
      <li>
        <svg viewBox="0 0 24 24" aria-hidden="true"><circle cx="12" cy="12" r="9" fill="none" stroke="#a8661f" stroke-width="2"/><path d="M3 12h18M12 3c3 3 3 15 0 18M12 3c-3 3-3 15 0 18" fill="none" stroke="#a8661f" stroke-width="1.5"/></svg>
        www.djmarlowk.net
      </li>
    </ul>
    <div class="brand-seal">
      <span class="brand-seal__name">Luminaire's</span>
    </div>
  </section>
</div>
</body>
</html>
```